Hydroponic Farm Needs a Business Card

We need a business card design for a hydroponic farm located on the Gulf Coast called 'Mossbrook Farms'. We grow many forms of lettuce and tomatoes along with other herbs and spices. We currently sell to farmer's markets though will soon be expanding to commercial accounts such as restaurants and grocery stores. The colors should be bright and vibrant to reflect the nature of our produce. The final design should communicate a professional, clean, yet friendly impression and able to be used both with farmer's markets and commercial accounts.

The pictures are an example of our product. The pictures do not have to be incorporated into the business card design.

Please put areas for information such as Names, Phone Number, E-mail address, and additional information.

Farm

```html
<!DOCTYPE html>
<html lang="en">
<head>
<meta charset="utf-8">
<title>Mossbrook Farms – Business Card</title>
<link rel="stylesheet" href="https://fonts.googleapis.com/css2?family=Source+Sans+3:wght@400;600;900&display=swap">
<style>
  :root {
    --stage: #e9e7e3;
    --soil: #7a2e1c;
    --soil-dark: #5e2314;
    --grass-light: #8fdc4a;
    --grass-mid: #4fb82a;
    --grass-dark: #2f8a17;
    --paper: #ffffff;
    --paper-grey: #ececec;
    --ink: #222222;
    --logo-dark: #2a2a2a;
    --icon-bg: #1c1c1c;
  }
  * { box-sizing: border-box; margin: 0; padding: 0; }
  html, body {
    width: 1200px; height: 873px; overflow: hidden;
    background: var(--stage);
    font-family: "Source Sans 3", Arial, sans-serif;
  }
  .canvas {
    position: relative; width: 1200px; height: 873px;
    display: flex; align-items: center; justify-content: center; gap: 40px;
  }
  .card {
    position: relative; width: 520px; height: 297px; overflow: hidden;
    box-shadow: 0 6px 18px rgba(0,0,0,.18);
  }
  .grass-band {
    position: absolute; left: 0; right: 0;
    background: linear-gradient(to bottom, var(--grass-light), var(--grass-mid) 55%, var(--grass-dark));
  }

  /* Front: contact side */
  .card--front { background: var(--soil); }
  .card--front .grass-band { top: 0; height: 50px; }
  .card--front .logo {
    position: absolute; right: 22px; top: 62px;
    font-weight: 900; font-size: 34px; letter-spacing: 1px;
    color: var(--paper); text-transform: uppercase; line-height: 1;
  }
  .info-panel {
    position: absolute; left: 18px; right: 18px; top: 112px; bottom: 18px;
    background: var(--paper); padding: 14px 18px;
  }
  .contact-list { list-style: none; display: flex; flex-direction: column; gap: 8px; }
  .contact-row {
    display: flex; align-items: center; gap: 12px;
    font-size: 14px; color: var(--ink);
  }
  .contact-row--name { font-weight: 600; }
  .contact-icon { width: 20px; height: 20px; flex: none; }

  /* Back: brand side */
  .card--back { background: linear-gradient(to bottom, var(--paper), var(--paper-grey)); }
  .card--back .logo {
    position: absolute; right: 34px; top: 58px;
    font-weight: 900; font-size: 38px; letter-spacing: 1px;
    color: var(--logo-dark); text-transform: uppercase; line-height: 1;
  }
  .card--back .grass-band { top: 150px; height: 52px; }
  .soil-band {
    position: absolute; left: 0; right: 0; top: 202px; bottom: 0;
    background: linear-gradient(to bottom, var(--soil), var(--soil-dark));
  }
</style>
</head>
<body>
<main class="canvas">

  <section class="card card--front" aria-label="Business card, contact side">
    <div class="grass-band" role="img" aria-label="Illustrated strip of green grass"></div>
    <p class="logo">Mossbrook Farms</p>
    <div class="info-panel">
      <ul class="contact-list">
        <li class="contact-row contact-row--name">
          <svg class="contact-icon" viewBox="0 0 20 20" aria-hidden="true">
            <rect width="20" height="20" rx="4" fill="var(--icon-bg)"/>
            <circle cx="10" cy="7.5" r="3.2" fill="#fff"/>
            <path d="M4 16.5c0-3.4 2.7-5.3 6-5.3s6 1.9 6 5.3z" fill="#fff"/>
          </svg>
          Personal Name
        </li>
        <li class="contact-row">
          <svg class="contact-icon" viewBox="0 0 20 20" aria-hidden="true">
            <rect width="20" height="20" rx="4" fill="var(--icon-bg)"/>
            <path d="M6.2 4.5l2 2.4-1.1 1.4c.8 1.7 2 2.9 3.6 3.7l1.4-1.1 2.4 2-1.2 2c-4.6-.4-8.1-3.9-8.5-8.5z" fill="#fff"/>
          </svg>
          01111 111111
        </li>
        <li class="contact-row">
          <svg class="contact-icon" viewBox="0 0 20 20" aria-hidden="true">
            <rect width="20" height="20" rx="4" fill="var(--icon-bg)"/>
            <circle cx="10" cy="10" r="2.6" fill="none" stroke="#fff" stroke-width="1.6"/>
            <path d="M12.6 8v3c0 1.3 2.2 1.6 2.2-1a4.8 4.8 0 1 0-1.9 3.8" fill="none" stroke="#fff" stroke-width="1.6"/>
          </svg>
          email@adress.com
        </li>
      </ul>
    </div>
  </section>

  <section class="card card--back" aria-label="Business card, brand side">
    <p class="logo">Mossbrook Farms</p>
    <div class="grass-band" role="img" aria-label="Illustrated strip of green grass"></div>
    <div class="soil-band"></div>
  </section>

</main>
</body>
</html>
```